Stunning Podcast Cover Design for The Morning Harbor Hour!!

I need a design for my new podcast.
I will need it in a variety of size/formats, such as a large version for my podcast website homepage, the thumbnail for Tunewell, Pondcast, Vexa Stream and more.

The podcast is called "The Morning Harbor Hour" and it includes topics such as: business, entrepreneurship, finance, budgeting, estate planning, end-of-life planning, travel, business and personal stories featuring people from all over the world, life in general, and more.

I don't have a vision in mind so am looking for creativity but it definitely needs to have the colour gold in it somewhere! No cartoon characters please.

I will provide comments/feedback to each designer.

***UPDATE: Please see some photos of me that can be used in the podcast design.

Here is some tips on creating podcast designs. https://www.castleafy.example/blog/10-tips-create-awesome-podcast-artwork

Target Market(s)

Adults 25 - 65

Font styles to use
Other font styles liked:
• something modern - see my company logo as an example

Colors

Designer to choose colors to be used in the design.

Requirements
Must have
• The colour gold in it
Nice to have
• I feel like the word "The" should be smaller then the other three words.
• I would like to see designs with a white coloured background and a black coloured one also...
• Perhaps designs with a filter over the photo, and without.
• Perhaps use my photo, or don't use my photo!
• Please see some photos of me that can be used in the podcast design.
• Here is some tips on creating podcast designs. https://www.castleafy.example/blog/10-tips-create-awesome-podcast-artwork
Should not have
• cartoon characters
• Corny 1990's "Evenings Among the Gilded and Glamorous" look - see https://www.vidorama.example/watch?v=Q7T2KX8PLBZ

```html
<!DOCTYPE html>
<html lang="en">
<head>
<meta charset="utf-8">
<title>The Morning Harbor Hour</title>
<link rel="stylesheet" href="https://fonts.googleapis.com/css2?family=Playfair+Display:wght@400;500&display=swap">
<style>
  :root {
    --forest-deep: #06140b;
    --forest-mid: #0f3a1b;
    --forest-light: #1f6a30;
    --title-white: #ffffff;
    --gold-dark: #a86d1c;
    --gold-mid: #d9a443;
    --gold-light: #f8e8a6;
  }
  * { margin: 0; padding: 0; box-sizing: border-box; }
  html, body {
    width: 1200px;
    height: 1200px;
    overflow: hidden;
    background: var(--forest-deep);
  }
  .cover {
    position: relative;
    width: 1200px;
    height: 1200px;
    overflow: hidden;
    font-family: "Playfair Display", Georgia, serif;
  }
  .cover__foliage {
    position: absolute;
    inset: 0;
    background:
      radial-gradient(ellipse 55% 45% at 30% 30%, rgba(40, 120, 55, 0.55), transparent 70%),
      radial-gradient(ellipse 50% 40% at 75% 35%, rgba(45, 130, 60, 0.5), transparent 70%),
      radial-gradient(ellipse 60% 45% at 30% 85%, rgba(30, 100, 45, 0.5), transparent 70%),
      radial-gradient(ellipse 45% 35% at 85% 80%, rgba(35, 110, 50, 0.45), transparent 70%),
      radial-gradient(ellipse 80% 80% at 50% 50%, var(--forest-mid), var(--forest-deep));
  }
  .title {
    position: absolute;
    inset: 0;
    text-align: center;
    font-weight: 400;
    color: var(--title-white);
  }
  .title__line {
    position: absolute;
    left: 0;
    right: 0;
    line-height: 1;
    white-space: nowrap;
    text-shadow: 0 2px 12px rgba(0, 0, 0, 0.35);
  }
  .title__line--small {
    top: 240px;
    font-size: 86px;
    letter-spacing: 2px;
  }
  .title__line--main {
    font-size: 172px;
    letter-spacing: -2px;
  }
  .title__line--first { top: 350px; }
  .title__line--second { top: 552px; }
  .title__line--gold {
    top: 760px;
    background: linear-gradient(90deg, var(--gold-dark) 0%, var(--gold-mid) 25%, var(--gold-light) 50%, var(--gold-mid) 72%, var(--gold-dark) 100%);
    -webkit-background-clip: text;
    background-clip: text;
    color: transparent;
    text-shadow: none;
    width: fit-content;
    margin: 0 auto;
  }
</style>
</head>
<body>
  <main class="cover">
    <div class="cover__foliage" role="img" aria-label="Close-up photograph of dark green fern fronds filling the background"></div>
    <h1 class="title">
      <span class="title__line title__line--small">THE</span>
      <span class="title__line title__line--main title__line--first">MORNING</span>
      <span class="title__line title__line--main title__line--second">HARBOR</span>
      <span class="title__line title__line--main title__line--gold">HOUR</span>
    </h1>
  </main>
</body>
</html>
```